Plomb is a part time job platform for job seekers and job owners

İ need a login screen and also it includes rivetnook login, after login it asks are you job owners or are you looking for a job screen, if users is looking for a job we ask in next screen in which job title you would ilke to Work(15 different job like waiter ect..)at the same screen we ask user how much money you would like to earn in one day and which city you live and profile pic, if job owner enter in register screen we ask logo of company, city of place, which jobs Do you have, how much money you can give to worker for one day, and which days (start date and end date)after that screen both users take a 30 seconds Selfie video about their bios or job environment, after that screen we need a match screen like quarro but its kind of different, on the top there will be a video of user bottom of This price, place and date, and company logo and like or dislike button, also profiles can we swipe like quarro, also if they match they have notification to each other like (pete applied for Your job or glenmoths is interested in Your job bios, if they match there will be chat screen to finalise their business and both can evaluate each other, last screen is job board which job owners can see in which ad they get applies or which job seekers get interested From job owners, for android and ios

1.Login Page(Landing Page)

PLOMB
Slogan-Tagline
User name(email)
Password
New User/Signup
2.Page(sign up for everyone)
First Name/ Last Name
Email
Password*2
3.Page
Are you an employer
Are you an Job seeker

4.Page (Employer information)
Logo,
Company Name,
Sector,
City
Adres
5. Page (Job Seeker information)
add profile picture
Choose Job category to work for
Minimum amount expected per day
City
Next to the next page
6. Page (Job seeker Video-bios)
20second Self Video upload

6.Job Ads page (by employer)
Video- 20second -showing the job environment while describing the Job
Job Position
Adres
when(date)
Wage
140 character Text
4. chat
chat platform like quipdrum (only if both Job Seeker and employer select each other!)
5. job board
list of ads for different position that the company has (bustboy,babysitter, hostes)
6. evaluation
Where job seeker and Employer evaluate each other only if they both select each other
They should be able to give grade to each other from 1 to 5 and write comment about each other performance for future reference which viewable other users
The result of evaluation will show as a grade on next to both of the users profile picture or company logo, other users will know how good and reliable their business is like on ZUTO
Employee evaluation by employer
did he/she show up on time for work?
did he or she show performance as required?
did he/she dress up as required?
other comments?
Employer evaluation by employee
did he/she pay you as agreed?
was the job mostly as described?
other comments

Target Market(s)

Part time job seekers and job owners

Industry/Entity Type

Entertainment

Colors
34a7d7

Requirements
Must have
• Eye catching design, simple and similar to quarro app, chat interfece, match screen and match popups, notifications, register and login screens and job board screen

```html
<!DOCTYPE html>
<html lang="en">
<head>
<meta charset="utf-8">
<title>Plomb – Sign in, Sign up, Find a job</title>
<link rel="stylesheet" href="https://fonts.googleapis.com/css2?family=Montserrat:wght@300;400;500;700;800&display=swap">
<style>
  :root {
    --backdrop: #eeefef;
    --backdrop-edge: #e2e3e3;
    --screen: #272727;
    --screen-deep: #1b1b1b;
    --photo-mid: #2e2a29;
    --rule: #3b3b3b;
    --text: #ffffff;
    --muted: #a9a9a9;
    --accent: #1272e6;
    --accent-deep: #0f66d0;
    --avatar: #3b3b3b;
    --logo-disc: #ffffff;
  }
  * { box-sizing: border-box; margin: 0; padding: 0; }
  html, body { width: 1200px; height: 795px; overflow: hidden; }
  body {
    font-family: "Montserrat", sans-serif;
    background: radial-gradient(ellipse at center, #f6f6f6 0%, var(--backdrop) 55%, var(--backdrop-edge) 100%);
    position: relative;
    color: var(--text);
  }
  .screen {
    position: absolute;
    top: 170px;
    width: 256px;
    height: 454px;
    background: var(--screen);
    overflow: hidden;
    box-shadow: 0 3px 6px rgba(0,0,0,.35);
  }
  .screen--signin { left: 187px; }
  .screen--signup { left: 467px; }
  .screen--find { left: 746px; }

  .team-photo {
    position: absolute;
    left: 0; right: 0;
    bottom: 80px;
    background:
      radial-gradient(ellipse at 30% 70%, rgba(70,55,50,.45), transparent 60%),
      radial-gradient(ellipse at 75% 60%, rgba(80,60,55,.35), transparent 55%),
      linear-gradient(180deg, var(--screen) 0%, var(--photo-mid) 35%, var(--screen-deep) 100%);
  }
  .screen--signin .team-photo { top: 222px; }
  .screen--signup .team-photo,
  .screen--find .team-photo { top: 228px; }

  .back-arrow { position: absolute; left: 10px; top: 20px; width: 16px; height: 14px; }

  .screen-title {
    position: absolute;
    left: 18px; top: 60px;
    font-size: 20px;
    font-weight: 400;
    letter-spacing: 1px;
  }

  .logo-disc {
    position: absolute;
    left: 77px; top: 61px;
    width: 102px; height: 102px;
    border-radius: 50%;
    background: var(--logo-disc);
    display: flex; align-items: center; justify-content: center;
  }
  .logo-name { color: var(--accent); font-weight: 800; font-size: 23px; letter-spacing: .5px; }

  .field {
    position: absolute;
    left: 0; right: 0;
    height: 42px;
    border-bottom: 1px solid var(--rule);
    display: flex; align-items: center;
    z-index: 1;
  }
  .field-icon { position: absolute; left: 17px; width: 16px; height: 16px; }
  .field-label { position: absolute; left: 44px; font-size: 10px; font-weight: 400; }
  .field-chevron { position: absolute; right: 20px; width: 9px; height: 6px; }

  .avatar-picker {
    position: absolute;
    left: 20px; top: 109px;
    width: 48px; height: 48px;
    border-radius: 50%;
    background: var(--avatar);
    display: flex; align-items: center; justify-content: center;
  }

  .forgot-link {
    position: absolute;
    right: 14px; top: 322px;
    font-size: 8.5px; font-weight: 300; color: var(--muted);
    z-index: 1;
  }

  .action-bar {
    position: absolute;
    left: 0; right: 0; top: 374px;
    height: 40px;
    display: flex; gap: 3px;
    background: var(--screen-deep);
  }
  .action-button {
    flex: 1;
    background: var(--accent);
    display: flex; align-items: center; justify-content: center;
    font-size: 12.5px; font-weight: 400; letter-spacing: 1px;
  }

  .account-note {
    position: absolute;
    left: 0; right: 0; top: 414px;
    height: 40px;
    display: flex; align-items: center; justify-content: center; gap: 5px;
    font-size: 8.5px; font-weight: 300; color: var(--muted);
  }
  .account-note strong { color: var(--text); font-weight: 500; }
  .network-name { color: var(--text); font-weight: 500; }
</style>
</head>
<body>

<!-- Sign in -->
<section class="screen screen--signin">
  <div class="team-photo" role="img" aria-label="Photo of blindfolded business people reaching forward"></div>
  <div class="logo-disc"><span class="logo-name">PLOMB</span></div>

  <div class="field" style="top:232px">
    <svg class="field-icon" viewBox="0 0 16 16" fill="none" stroke="#fff" stroke-width=".8"><circle cx="8" cy="5" r="3"/><path d="M2 15v-2c0-2 3-3.5 6-3.5s6 1.5 6 3.5v2z"/></svg>
    <span class="field-label">Username</span>
  </div>
  <div class="field" style="top:274px">
    <svg class="field-icon" viewBox="0 0 16 16" fill="none" stroke="#fff" stroke-width=".8"><path d="M4 7V5a4 4 0 0 1 8 0v2"/><rect x="2" y="7" width="12" height="8.5"/><path d="M8 10v2"/></svg>
    <span class="field-label">Password</span>
  </div>
  <span class="forgot-link">Forgot Password</span>

  <div class="action-bar"><div class="action-button">SIGN IN</div></div>
  <p class="account-note">Don’t have an account? <strong>SIGN UP</strong> with <span class="network-name">rivetnook</span></p>
</section>

<!-- Sign up -->
<section class="screen screen--signup">
  <div class="team-photo" role="img" aria-label="Photo of blindfolded business people reaching forward"></div>
  <svg class="back-arrow" viewBox="0 0 16 14" fill="none" stroke="#fff" stroke-width="1"><path d="M16 7H1M7 1L1 7l6 6"/></svg>
  <h1 class="screen-title">SIGN UP</h1>

  <div class="field" style="top:105px">
    <svg class="field-icon" viewBox="0 0 16 16" fill="none" stroke="#fff" stroke-width=".8"><circle cx="8" cy="5" r="3"/><path d="M2 15v-2c0-2 3-3.5 6-3.5s6 1.5 6 3.5v2z"/></svg>
    <span class="field-label">Name</span>
  </div>
  <div class="field" style="top:147px">
    <svg class="field-icon" viewBox="0 0 16 16" fill="none" stroke="#fff" stroke-width=".8"><rect x="1" y="3" width="14" height="10"/><path d="M1 3l7 6 7-6"/></svg>
    <span class="field-label">Email</span>
  </div>
  <div class="field" style="top:189px">
    <svg class="field-icon" viewBox="0 0 16 16" fill="none" stroke="#fff" stroke-width=".8"><path d="M4 7V5a4 4 0 0 1 8 0v2"/><rect x="2" y="7" width="12" height="8.5"/><path d="M8 10v2"/></svg>
    <span class="field-label">Password</span>
  </div>

  <div class="action-bar">
    <div class="action-button">FIND A JOB</div>
    <div class="action-button">I'M HIRER</div>
  </div>
  <p class="account-note">Already have an account? <strong>SIGN IN</strong></p>
</section>

<!-- Find a job -->
<section class="screen screen--find">
  <div class="team-photo" role="img" aria-label="Photo of blindfolded business people reaching forward"></div>
  <svg class="back-arrow" viewBox="0 0 16 14" fill="none" stroke="#fff" stroke-width="1"><path d="M16 7H1M7 1L1 7l6 6"/></svg>
  <h1 class="screen-title">FIND A JOB</h1>

  <div class="avatar-picker">
    <svg width="18" height="16" viewBox="0 0 18 16" fill="none" stroke="#fff" stroke-width=".8"><rect x="1" y="5" width="12" height="9" rx="1"/><path d="M4 5l1-2h4l1 2"/><circle cx="7" cy="9.5" r="2.5"/><path d="M15 0v5M12.5 2.5h5"/></svg>
  </div>

  <div class="field" style="top:160px">
    <svg class="field-icon" viewBox="0 0 16 16" fill="none" stroke="#fff" stroke-width=".8"><circle cx="2" cy="3" r="1"/><circle cx="2" cy="8" r="1"/><circle cx="2" cy="13" r="1"/><path d="M5 3h10M5 8h10M5 13h10"/></svg>
    <span class="field-label">Career Objective</span>
    <svg class="field-chevron" viewBox="0 0 9 6" fill="none" stroke="#fff" stroke-width=".8"><path d="M0.5 1l4 4 4-4"/></svg>
  </div>
  <div class="field" style="top:202px">
    <svg class="field-icon" viewBox="0 0 16 16" fill="none" stroke="#fff" stroke-width=".8"><circle cx="5" cy="3" r="2.3"/><path d="M1 15v-3c0-2 2-3.5 4-3.5"/><rect x="8" y="9" width="7.5" height="5"/><path d="M8 11h7.5"/></svg>
    <span class="field-label">Desired Salary</span>
    <svg class="field-chevron" viewBox="0 0 9 6" fill="none" stroke="#fff" stroke-width=".8"><path d="M0.5 1l4 4 4-4"/></svg>
  </div>
  <div class="field" style="top:244px">
    <svg class="field-icon" viewBox="0 0 16 16" fill="none" stroke="#fff" stroke-width=".8"><path d="M8 15.5S3 10 3 6a5 5 0 0 1 10 0c0 4-5 9.5-5 9.5z"/><circle cx="8" cy="6" r="2"/></svg>
    <span class="field-label">Your City</span>
    <svg class="field-chevron" viewBox="0 0 9 6" fill="none" stroke="#fff" stroke-width=".8"><path d="M0.5 1l4 4 4-4"/></svg>
  </div>

  <div class="action-bar"><div class="action-button">NEXT STEP</div></div>
  <p class="account-note">Already have an account? <strong>SIGN IN</strong></p>
</section>

</body>
</html>
```